依頼詳細
シンプルかつ先進的なアイデアを求めております。
一新したロゴも活用したいです。
記載項目
会社名・役職・氏名・郵便番号・住所・電話・FAX・携帯・メール・WEB・
希望イメージ
シンプル 複雑
単色 カラフル
暗い 明るい
日常 高級
遊び心 厳粛
未来的 伝統的
女性的 男性的
希望する色
グレー系
もう少し提案をいただいたうえで検討したいため、期間を延長させていただきます。
https://kawabaseiki.co.jp/

もう少しモダンなデザインを希望してます。
弊社HPもご参照ください。
宜しくお願いいたします。
■ 選んだ理由

イメージに合ったデザインである点

■ 提案者全員のお礼・コメント

何度もご提案頂き有難うございました、お陰でとても気に入ったデザインになりました。

```html
<!DOCTYPE html>
<html lang="ja">
<head>
<meta charset="utf-8">
<title>KAWABA 名刺デザイン</title>
<link href="https://fonts.googleapis.com/css2?family=Noto+Sans+JP:wght@400;500;700&display=swap" rel="stylesheet">
<style>
  :root {
    --page: #ffffff;
    --card-light: #ffffff;
    --card-dark: #3b3634;
    --ink: #2b2b2b;
    --ink-soft: #555555;
    --paper-ink: #ffffff;
    --paper-soft: #d8d5d3;
    --border: #9a9a9a;
  }
  * { margin: 0; padding: 0; box-sizing: border-box; }
  html, body {
    width: 1200px; height: 2404px; overflow: hidden;
    background: var(--page);
    font-family: "Noto Sans JP", sans-serif;
  }
  .sheet { position: relative; width: 1200px; height: 2404px; }
  .card { position: absolute; left: 128px; width: 1000px; }
  .card--front { top: 152px; height: 572px; background: var(--card-light); border: 2px solid var(--border); color: var(--ink); }
  .card--back { top: 888px; height: 572px; background: var(--card-dark); color: var(--paper-ink); }
  .card--plain { top: 1664px; height: 576px; background: var(--card-dark); color: var(--paper-ink); }

  .brand { position: absolute; display: flex; flex-direction: column; align-items: center; width: 240px; }
  .brand__mark { width: 112px; height: 112px; border-radius: 50%; border: 6px solid currentColor; }
  .brand__name { margin-top: 38px; font-size: 36px; font-weight: 700; letter-spacing: 2px; line-height: 1; }
  .brand__since { margin-top: 15px; font-size: 14px; font-weight: 700; letter-spacing: 1px; line-height: 1; }

  .card--front .brand { left: 128px; top: 290px; }
  .card--back .brand { left: 600px; top: 180px; }
  .card--plain .brand { left: 380px; top: 168px; }

  .info { position: absolute; line-height: 1; }
  .info__title { font-size: 20px; }
  .info__name { font-weight: 400; }
  .info__mobile { display: flex; align-items: center; gap: 12px; font-size: 24px; }
  .info__mobile svg { width: 14px; height: 24px; }
  .info__company { font-weight: 700; letter-spacing: 1px; }
  .info__lines { font-size: 21px; color: var(--ink-soft); }

  .card--front .info { left: 490px; top: 108px; }
  .card--front .info__name { margin-top: 38px; font-size: 48px; letter-spacing: 14px; }
  .card--front .info__mobile { margin-top: 33px; }
  .card--front .info__company { margin-top: 63px; font-size: 24px; }
  .card--front .info__lines { margin-top: 13px; line-height: 28px; }

  .card--back .info { left: 24px; top: 110px; }
  .card--back .info__name { margin-top: 36px; font-size: 44px; }
  .card--back .info__mobile { margin-top: 34px; }
  .card--back .info__company { margin-top: 55px; font-size: 30px; }
  .card--back .info__lines { margin-top: 8px; line-height: 30px; color: var(--paper-soft); }
</style>
</head>
<body>
<main class="sheet">

  <section class="card card--front" aria-label="名刺 表面（日本語）">
    <div class="brand">
      <span class="brand__mark"></span>
      <span class="brand__name">KAWABA</span>
      <span class="brand__since">SINCE 1958</span>
    </div>
    <div class="info">
      <p class="info__title">代表取締役</p>
      <p class="info__name">山田太郎</p>
      <p class="info__mobile">
        <svg viewBox="0 0 14 24" aria-hidden="true"><rect x="1.5" y="1.5" width="11" height="21" rx="2" fill="none" stroke="currentColor" stroke-width="2.5"/></svg>
        090-1234-5678
      </p>
      <p class="info__company">株式会社 KAWABA</p>
      <p class="info__lines">
        〒123-0000<br>
        ○○○○○○○○○○○○123<br>
        Tel. 000-000-0000　Fax. 000-000-0000<br>
        Mail. info@kawaba.example<br>
        URL. http://www.kawaba.example
      </p>
    </div>
  </section>

  <section class="card card--back" aria-label="名刺 裏面（英語）">
    <div class="info">
      <p class="info__title">CEO</p>
      <p class="info__name">Taro Yamada</p>
      <p class="info__mobile">
        <svg viewBox="0 0 14 24" aria-hidden="true"><rect x="1.5" y="1.5" width="11" height="21" rx="2" fill="none" stroke="currentColor" stroke-width="2.5"/></svg>
        +81-90-1234-5678
      </p>
      <p class="info__company">KAWABA Co., Ltd.</p>
      <p class="info__lines">
        123, ○○○○, ○○○○, ○○○○,<br>
        ○○○○, 123-0000, Japan<br>
        Tel. +81-00-000-0000　Fax. +81-00-000-0000<br>
        Mail. info@kawaba.example<br>
        URL. http://www.kawaba.example
      </p>
    </div>
    <div class="brand">
      <span class="brand__mark"></span>
      <span class="brand__name">KAWABA</span>
      <span class="brand__since">SINCE 1958</span>
    </div>
  </section>

  <section class="card card--plain" aria-label="名刺 ロゴ面">
    <div class="brand">
      <span class="brand__mark"></span>
      <span class="brand__name">KAWABA</span>
      <span class="brand__since">SINCE 1958</span>
    </div>
  </section>

</main>
</body>
</html>
```